Super urgent - business card design

I need to design a business card
on the front side the words "VORIAN PARTNERS" with the top half surrounded by a stylised cloud. Minimalist, navy blue font on white background, with the Vorian partners in embossing.

On the back contact details (avoid centered). I would rather have the details taking the 2/3rd on the right and having the logo on the left, but anyway not plain centered

Marcello Tavoletti
CEO e Fondatore

m.tavoletti@vorian-partners.example
+39.331.584.2064

Piazza Lunetti 7
20145 Milano

```html
<!DOCTYPE html>
<html lang="it">
<head>
<meta charset="UTF-8">
<title>Vorian Partners – Business Card</title>
<link href="https://fonts.googleapis.com/css2?family=Playfair+Display:wght@700&family=Inter:wght@400;500&display=swap" rel="stylesheet">
<style>
  :root {
    --backdrop: #d4d5d7;
    --navy: #16063f;
    --paper: #ffffff;
    --ink: #16063f;
  }
  * { box-sizing: border-box; margin: 0; padding: 0; }
  html, body {
    width: 1200px; height: 800px; overflow: hidden;
    background: var(--backdrop);
  }
  .canvas {
    width: 1200px; height: 800px;
    display: flex; flex-direction: column;
    align-items: center; justify-content: center;
    gap: 40px;
  }
  .card {
    width: 540px; height: 330px;
    border-radius: 18px;
    position: relative;
    box-shadow: 0 10px 28px rgba(0,0,0,0.18);
  }
  .card--front {
    background: var(--navy);
    display: flex; flex-direction: column;
    align-items: center; justify-content: center;
    gap: 22px;
  }
  .brand-dot {
    width: 70px; height: 70px; border-radius: 50%;
    background: var(--paper);
  }
  .brand-name {
    font-family: "Playfair Display", serif;
    font-weight: 700;
    letter-spacing: 0.02em;
  }
  .card--front .brand-name { color: var(--paper); font-size: 38px; }
  .card--back { background: var(--paper); color: var(--ink); }
  .back-brand {
    position: absolute; left: 34px; top: 128px;
    display: flex; flex-direction: column; align-items: flex-start; gap: 10px;
  }
  .back-brand .brand-dot { width: 34px; height: 34px; background: var(--navy); }
  .back-brand .brand-name { color: var(--ink); font-size: 17px; }
  .details {
    position: absolute; left: 236px; top: 56px;
    font-family: "Inter", sans-serif; font-size: 13.5px; line-height: 1.5;
  }
  .person-name {
    font-family: "Playfair Display", serif; font-weight: 700;
    font-size: 26px; line-height: 1.1;
  }
  .person-role { font-weight: 500; margin-bottom: 12px; }
  .address { margin-bottom: 14px; }
  .contact { list-style: none; }
  .contact li { display: flex; align-items: center; gap: 8px; margin-bottom: 4px; font-size: 13px; }
  .contact svg { width: 14px; height: 14px; flex: none; fill: var(--ink); }
</style>
</head>
<body>
<main class="canvas">
  <section class="card card--front" aria-label="Fronte del biglietto">
    <span class="brand-dot"></span>
    <span class="brand-name">VORIAN PARTNERS</span>
  </section>

  <section class="card card--back" aria-label="Retro del biglietto">
    <div class="back-brand">
      <span class="brand-dot"></span>
      <span class="brand-name">VORIAN PARTNERS</span>
    </div>
    <div class="details">
      <p class="person-name">Marcello Tavoletti</p>
      <p class="person-role">CEO e Fondatore</p>
      <p class="address">Piazza Lunetti 7<br>20145 Milano</p>
      <ul class="contact">
        <li>
          <svg viewBox="0 0 24 24" aria-hidden="true"><path d="M6.6 10.8a15.1 15.1 0 0 0 6.6 6.6l2.2-2.2c.3-.3.7-.4 1-.2 1.1.4 2.3.6 3.6.6.6 0 1 .4 1 1V20c0 .6-.4 1-1 1A17 17 0 0 1 3 4c0-.6.4-1 1-1h3.5c.6 0 1 .4 1 1 0 1.3.2 2.5.6 3.6.1.3 0 .7-.2 1z"/></svg>
          +39.331.584.2064
        </li>
        <li>
          <svg viewBox="0 0 24 24" aria-hidden="true"><path d="M2 5h20v14H2zM4 7v.5l8 5 8-5V7l-8 5z"/></svg>
          m.tavoletti@vorian-partners.example
        </li>
        <li>
          <svg viewBox="0 0 24 24" aria-hidden="true"><path d="M12 2a10 10 0 1 0 0 20 10 10 0 0 0 0-20zm6.9 6h-3a15 15 0 0 0-1.3-3.9A8 8 0 0 1 18.9 8zM12 4c.8 1.2 1.5 2.5 1.9 4h-3.8c.4-1.5 1.1-2.8 1.9-4zM4.3 14a8 8 0 0 1 0-4h3.4a16 16 0 0 0 0 4zm.8 2h3a15 15 0 0 0 1.3 3.9A8 8 0 0 1 5.1 16zm3-8h-3a8 8 0 0 1 4.3-3.9A15 15 0 0 0 8.1 8zM12 20c-.8-1.2-1.5-2.5-1.9-4h3.8c-.4 1.5-1.1 2.8-1.9 4zm2.3-6H9.7a14 14 0 0 1 0-4h4.6a14 14 0 0 1 0 4zm.3 5.9a15 15 0 0 0 1.3-3.9h3a8 8 0 0 1-4.3 3.9zm1.7-5.9a16 16 0 0 0 0-4h3.4a8 8 0 0 1 0 4z"/></svg>
          www.vorian-partners.example
        </li>
      </ul>
    </div>
  </section>
</main>
</body>
</html>
```